Letterhead design for Sleep Consulting Business

I'm looking for a new letterhead (heading/footer) design for my Sleep Consulting Business, I work with families to help their children improve their sleep.

The heading/footer will used in Microsoft Word Only-to be used for all of my documents such as writing Sleep Plans. I need to utilize as much working space in the document as possible. This will NOT be printed out on paper- it will only be used for heading/footer on microsoft word, then emailed to clients, who may print it at home.

My brand colors:
Dark Blue Hex: 1F2A42
Lighter Blueish Hex: 90BEC9
You're welcome to check out my website for inspiration- it is freshly created with other colors as well, and I love the outcome. www.hollowpinerest.com

Target Market(s)

Tired parents

Font styles to use
Script
Other font styles liked:
• Great Vibe, Lato or Just Another Hand are all used currently for my brand. Open to other options.

Requirements
Must have
• The letterhead (heading/footer) MUST be kept narrow (height-wise), so I have plenty of space on my document, while including important information.

It should look professional on screen, and when printed.

Must include my business name OR logo (Hollow Pine Sleep Consulting), and my email address. Mara@hollowpinerest.com

Website is optional, not required, just if you need to fill in a spot: www.hollowpinerest.com

```html
<!DOCTYPE html>
<html lang="en">
<head>
<meta charset="UTF-8">
<title>Hollow Pine Sleep Consulting – Letterhead</title>
<link rel="stylesheet" href="https://fonts.googleapis.com/css2?family=Lato:wght@400;700&family=Tinos&display=swap">
<style>
  :root {
    --brand-navy: #1f2a42;
    --brand-mist: #90bec9;
    --backdrop: #e4e7ea;
    --sheet: #ffffff;
    --body-ink: #6d6f73;
    --heading-ink: #2b2d31;
  }
  * { margin: 0; padding: 0; box-sizing: border-box; }
  html, body {
    width: 1200px; height: 900px; overflow: hidden;
    background: var(--backdrop);
  }
  .letterhead {
    position: absolute; left: 296px; top: 20px;
    width: 608px; height: 860px;
    background: var(--sheet);
    box-shadow: 0 2px 10px rgba(0,0,0,0.18);
    font-family: "Lato", sans-serif;
    overflow: hidden;
  }
  .letterhead__waves { position: absolute; inset: 0; width: 100%; height: 100%; }
  .brand {
    position: absolute; left: 59px; top: 39px;
    display: flex; align-items: center; gap: 10px;
  }
  .brand__dot {
    width: 46px; height: 46px; border-radius: 50%;
    background: var(--brand-mist);
  }
  .brand__name {
    font-family: "Lato", sans-serif; font-weight: 400;
    font-size: 17px; color: var(--brand-navy); letter-spacing: 0.3px;
  }
  .salutation-row {
    position: absolute; left: 59px; right: 59px; top: 213px;
    display: flex; justify-content: space-between;
    font-size: 8px; font-weight: 700; color: var(--heading-ink);
  }
  .letter-body {
    position: absolute; left: 59px; right: 59px; top: 260px;
    font-size: 7.6px; line-height: 13.4px; color: var(--body-ink);
    text-align: justify;
  }
  .letter-body p + p { margin-top: 13px; }
  .contact {
    position: absolute; left: 59px; top: 824px;
    font-family: "Tinos", serif; font-size: 10px; line-height: 12.5px;
    color: var(--brand-navy);
  }
  .contact__line { display: flex; align-items: center; gap: 6px; }
  .contact__icon { width: 8px; height: 8px; }
</style>
</head>
<body>
  <main class="letterhead">
    <svg class="letterhead__waves" viewBox="0 0 818 1157" preserveAspectRatio="none" aria-hidden="true">
      <!-- header -->
      <path d="M0,12 C250,0 450,58 818,40" fill="none" stroke="var(--brand-mist)" stroke-width="4"/>
      <path d="M0,24 C260,8 470,66 818,50 L818,88 C560,102 320,22 0,31 Z" fill="var(--brand-navy)"/>
      <path d="M330,44 C480,88 650,97 818,93" fill="none" stroke="var(--brand-mist)" stroke-width="2.5"/>
      <!-- footer -->
      <path d="M0,1071 C150,1058 300,1062 420,1084" fill="none" stroke="var(--brand-mist)" stroke-width="2.5"/>
      <path d="M0,1080 C150,1060 350,1070 500,1104 C620,1128 720,1134 818,1124 L818,1131 C700,1146 580,1142 450,1122 C300,1101 150,1100 0,1114 Z" fill="var(--brand-navy)"/>
      <path d="M0,1119 C200,1100 350,1116 500,1136 C620,1151 720,1153 818,1141" fill="none" stroke="var(--brand-mist)" stroke-width="3"/>
    </svg>

    <header class="brand">
      <span class="brand__dot"></span>
      <span class="brand__name">Hollow Pine Sleep Consulting</span>
    </header>

    <div class="salutation-row">
      <span class="salutation">Dear Client,</span>
      <span class="letter-date">Date: 16.02.2021</span>
    </div>

    <section class="letter-body">
      <p>Lorem Ipsum is simply dummy text of the printing and typesetting industry. Lorem Ipsum has been the industry's standard dummy text ever since the 1500s, when an unknown printer took a galley of type and scrambled it to make a type specimen book. It has survived not only five centuries, but also the leap into electronic typesetting, remaining essentially unchanged. It was popularised in the 1960s with the release of Typeleaf sheets containing Lorem Ipsum passages, and more recently with desktop publishing software like Pressline Composer including versions of Lorem Ipsum. It is a long established fact that a reader will be distracted by the readable content of a page when looking at its layout. The point of using Lorem Ipsum is that it has a more-or-less normal distribution of letters, as opposed to using 'Content here, content here', making it look like readable English. Many desktop publishing packages and web page editors now use Lorem Ipsum as their default model text, and a search for 'lorem ipsum' will uncover many web sites still in their infancy. Various versions have evolved over the years, sometimes by accident, sometimes on purpose (injected humour and the like).</p>
      <p>Contrary to popular belief, Lorem Ipsum is not simply random text. It has roots in a piece of classical Latin literature from 45 BC, making it over 2000 years old. Daniel Harrow, a Latin professor at Alder Ridge College in Vermont, looked up one of the more obscure Latin words, consectetur, from a Lorem Ipsum passage, and going through the cites of the word in classical literature, discovered the undoubtable source. Lorem Ipsum comes from sections 1.10.32 and 1.10.33 of "de Finibus Bonorum et Malorum" (The Extremes of Good and Evil) by Lucius Verranus, written in 45 BC. This book is a treatise on the theory of ethics, very popular during the Renaissance. The first line of Lorem Ipsum, "Lorem ipsum dolor sit amet..", comes from a line in section 1.10.32.</p>
      <p>There are many variations of passages of Lorem Ipsum available, but the majority have suffered alteration in some form, by injected humour, or randomised words which don't look even slightly believable. If you are going to use a passage of Lorem Ipsum, you need to be sure there isn't anything embarrassing hidden in the middle of text. All the Lorem Ipsum generators on the Internet tend to repeat predefined chunks as necessary, making this the first true generator on the Internet. It uses a dictionary of over 200 Latin words, combined with a handful of model sentence structures, to generate Lorem Ipsum which looks reasonable. The generated Lorem Ipsum is therefore always free from repetition, injected humour, or non-characteristic words etc.</p>
      <p>There are many variations of passages of Lorem Ipsum available, but the majority have suffered alteration in some form, by injected humour, or randomised words which don't look even slightly believable. If you are going to use a passage of Lorem Ipsum, you need to be sure there isn't anything embarrassing hidden in the middle of text.</p>
    </section>

    <footer class="contact">
      <div class="contact__line">
        <svg class="contact__icon" viewBox="0 0 10 8" aria-hidden="true"><rect x="0.5" y="0.5" width="9" height="7" fill="none" stroke="var(--brand-mist)"/><path d="M0.5,0.8 L5,4.5 L9.5,0.8" fill="none" stroke="var(--brand-mist)"/></svg>
        <span>Mara@hollowpinerest.com</span>
      </div>
      <div class="contact__line">
        <svg class="contact__icon" viewBox="0 0 10 10" aria-hidden="true"><circle cx="5" cy="5" r="4.5" fill="none" stroke="var(--brand-mist)"/><ellipse cx="5" cy="5" rx="2" ry="4.5" fill="none" stroke="var(--brand-mist)" stroke-width="0.8"/><path d="M0.5,5 H9.5" stroke="var(--brand-mist)" stroke-width="0.8"/></svg>
        <span>www.hollowpinerest.com</span>
      </div>
    </footer>
  </main>
</body>
</html>
```